Email signature design - law firm

We are a small boutique law firm which is located near the beach in Manly, Australia.

We have just recently developed a new logo and are looking to redesign our letterhead, business cards and email signatures.

This brief is for our email signatures. This is an email signature to appear at the bottom of our Outlook emails so we would like it to be text that we are able to edit as the wording in our email signature often required amendments.

I have attached a word document which had our new logo, and our previous email signature which all the information/wording that needs to be included.

We would like multiple designs with a modern, simplistic yet striking look.

Thanks.

font - raleway or montserrat

Need extra days to review

• Must have the exact wording which appears in the email signature in the word document attached to brief.
• Must be able to edit the text as it is for an Outlook email signature which wording will change from time to time.

```html
<!DOCTYPE html>
<html lang="en">
<head>
<meta charset="utf-8">
<title>Carrow &amp; Bellamy Stationery</title>
<link rel="stylesheet" href="https://fonts.googleapis.com/css2?family=Montserrat:wght@600;700&family=Open+Sans:wght@400&display=swap">
<style>
  :root {
    --board: #9b9b9b;
    --paper: #fafafa;
    --navy: #3b4796;
    --rule: #56649f;
    --ink: #333338;
    --icon: #4a5aa3;
  }
  * { box-sizing: border-box; margin: 0; padding: 0; }
  html, body { width: 939px; height: 1200px; overflow: hidden; }
  body {
    position: relative;
    background: var(--board);
    font-family: "Open Sans", Arial, sans-serif;
    color: var(--ink);
  }
  .sheet {
    position: absolute;
    left: 171px;
    width: 597px;
    background: var(--paper);
    border: 1px solid #d0d0d0;
  }
  .business-card { top: 77px; height: 156px; }
  .letterhead { top: 265px; height: 846px; }

  .firm-name {
    position: absolute;
    left: 44px;
    font-family: "Montserrat", Arial, sans-serif;
    font-weight: 700;
    font-size: 12.5px;
    letter-spacing: 0.9px;
    color: var(--ink);
    white-space: nowrap;
  }
  .business-card .firm-name { top: 98px; }
  .letterhead .firm-name { top: 124px; }

  .header-rule { position: absolute; left: 0; width: 597px; height: 160px; overflow: visible; }
  .business-card .header-rule { top: 0; }
  .letterhead .header-rule { top: 26px; }

  .person { position: absolute; left: 227px; top: 41px; }
  .person-name {
    font-family: "Montserrat", Arial, sans-serif;
    font-weight: 700;
    font-size: 15.5px;
    color: var(--navy);
    line-height: 1.2;
  }
  .person-role { font-size: 8.5px; color: var(--ink); margin-top: 1px; }

  .contact {
    position: absolute;
    right: 43px;
    text-align: right;
    font-size: 10.6px;
    line-height: 15px;
    white-space: nowrap;
  }
  .business-card .contact { top: 23px; }
  .letterhead .contact { top: 49px; }
  .address { margin-bottom: 17px; }
  .contact-line { display: flex; align-items: center; justify-content: flex-end; gap: 4px; height: 15.3px; }
  .contact-icon { width: 11px; height: 11px; flex: none; }
</style>
</head>
<body>

<section class="sheet business-card">
  <p class="firm-name">Carrow &amp; Bellamy</p>
  <svg class="header-rule" viewBox="0 0 597 160" aria-hidden="true">
    <polyline points="44,92 336,92 382,62 553,62" fill="none" stroke="var(--rule)" stroke-width="1"/>
  </svg>
  <div class="person">
    <p class="person-name">Nadia Whitfield</p>
    <p class="person-role">Managing Director</p>
  </div>
  <div class="contact">
    <div class="address">Suite 4, 12 Tidewell Road<br>Seacliff NSW 2999</div>
    <div class="contact-line">(02) 5550 1842
      <svg class="contact-icon" viewBox="0 0 12 12"><circle cx="6" cy="6" r="5.3" fill="none" stroke="var(--icon)" stroke-width="0.9"/><path d="M3.3 5.2h5.4L8 7.8H4z" fill="var(--icon)"/></svg></div>
    <div class="contact-line">(02) 5550 1843
      <svg class="contact-icon" viewBox="0 0 12 12"><circle cx="6" cy="6" r="5.3" fill="none" stroke="var(--icon)" stroke-width="0.9"/><rect x="3.3" y="4.3" width="5.4" height="3.6" fill="var(--icon)"/></svg></div>
    <div class="contact-line">nadia.whitfield@carrowlaw.com.au
      <svg class="contact-icon" viewBox="0 0 12 12"><circle cx="6" cy="6" r="5.3" fill="none" stroke="var(--icon)" stroke-width="0.9"/><circle cx="6" cy="6" r="2.6" fill="none" stroke="var(--icon)" stroke-width="0.8"/><path d="M3.4 6h5.2M6 3.4v5.2" stroke="var(--icon)" stroke-width="0.6"/></svg></div>
    <div class="contact-line">www.carrowandbellamy.com.au
      <svg class="contact-icon" viewBox="0 0 12 12"><circle cx="6" cy="6" r="5.3" fill="none" stroke="var(--icon)" stroke-width="0.9"/><circle cx="6" cy="6" r="2.6" fill="none" stroke="var(--icon)" stroke-width="0.8"/><path d="M3.4 6h5.2M6 3.4v5.2" stroke="var(--icon)" stroke-width="0.6"/></svg></div>
  </div>
</section>

<section class="sheet letterhead">
  <p class="firm-name">Carrow &amp; Bellamy</p>
  <svg class="header-rule" viewBox="0 0 597 160" aria-hidden="true">
    <polyline points="44,94 336,94 382,63 553,63" fill="none" stroke="var(--rule)" stroke-width="1"/>
  </svg>
  <div class="contact">
    <div class="address">Suite 4, 12 Tidewell Road<br>Seacliff NSW 2999</div>
    <div class="contact-line">(02) 5550 1842
      <svg class="contact-icon" viewBox="0 0 12 12"><circle cx="6" cy="6" r="5.3" fill="none" stroke="var(--icon)" stroke-width="0.9"/><path d="M3.3 5.2h5.4L8 7.8H4z" fill="var(--icon)"/></svg></div>
    <div class="contact-line">(02) 5550 1843
      <svg class="contact-icon" viewBox="0 0 12 12"><circle cx="6" cy="6" r="5.3" fill="none" stroke="var(--icon)" stroke-width="0.9"/><rect x="3.3" y="4.3" width="5.4" height="3.6" fill="var(--icon)"/></svg></div>
    <div class="contact-line">nadia.whitfield@carrowlaw.com.au
      <svg class="contact-icon" viewBox="0 0 12 12"><circle cx="6" cy="6" r="5.3" fill="none" stroke="var(--icon)" stroke-width="0.9"/><circle cx="6" cy="6" r="2.6" fill="none" stroke="var(--icon)" stroke-width="0.8"/><path d="M3.4 6h5.2M6 3.4v5.2" stroke="var(--icon)" stroke-width="0.6"/></svg></div>
    <div class="contact-line">www.carrowandbellamy.com.au
      <svg class="contact-icon" viewBox="0 0 12 12"><circle cx="6" cy="6" r="5.3" fill="none" stroke="var(--icon)" stroke-width="0.9"/><circle cx="6" cy="6" r="2.6" fill="none" stroke="var(--icon)" stroke-width="0.8"/><path d="M3.4 6h5.2M6 3.4v5.2" stroke="var(--icon)" stroke-width="0.6"/></svg></div>
  </div>
</section>

</body>
</html>
```